Criminal Defense Law Firm needs Stationary design Theme for a Business Card, Envelope, and Letterhea

Our Law Firm is seeking a general design concept for a business card, letterhead, and Envelope.

Our website is WillowcrestTrialDesk.com

A design for these three items is requested to keep branding in place for the firm. Would like to keep the Firm Colors on the website consistent with our branding on business cards, letterheads, and mailing envelopes #10 size to be exact.

We would like business cards printed front and back with Law firm Colors from website.

Letterhead with law firm colors as well. Design is not limited to just the header, but the footer can be utilized as well for email, website, phone, fax, etc.

Simple #10 envelope consisting of the same design principles set out in the previous two designs.

```html
<!DOCTYPE html>
<html lang="en">
<head>
<meta charset="utf-8">
<title>Willowcrest Criminal Law Offices – Business Card</title>
<link href="https://fonts.googleapis.com/css2?family=Libre+Baskerville&family=Source+Sans+3:wght@400;500&display=swap" rel="stylesheet">
<style>
  :root {
    --backdrop: #e6e3de;
    --card-light: #e9e9e9;
    --card-dark: #1e1e1e;
    --ink: #1f1f1f;
    --gold: #a8905e;
    --teal: #1b9aaa;
    --serif: "Libre Baskerville", Georgia, serif;
    --sans: "Source Sans 3", Arial, sans-serif;
  }
  * { box-sizing: border-box; margin: 0; padding: 0; }
  html, body { width: 1200px; height: 900px; overflow: hidden; }
  body {
    background: var(--backdrop);
    position: relative;
    font-family: var(--sans);
  }
  .card {
    position: absolute;
    width: 525px;
    height: 300px;
    top: 300px;
    box-shadow: 0 6px 18px rgba(0,0,0,.18);
  }
  /* Back side */
  .card-back {
    left: 50px;
    background: var(--card-dark);
    display: flex;
    flex-direction: column;
    align-items: center;
    justify-content: center;
    gap: 34px;
  }
  .back-mark {
    display: flex;
    align-items: center;
    gap: 12px;
    color: var(--gold);
    font-family: var(--serif);
    font-size: 22px;
    letter-spacing: .04em;
  }
  .back-mark .dot {
    width: 18px; height: 18px;
    border: 2px solid var(--gold);
    border-radius: 50%;
  }
  .back-message {
    color: var(--gold);
    font-family: var(--serif);
    font-size: 15px;
    line-height: 1.45;
    text-align: center;
  }
  /* Front side */
  .card-front {
    left: 625px;
    background: var(--card-light);
    color: var(--ink);
    padding: 34px 36px;
  }
  .firm {
    display: flex;
    align-items: center;
    gap: 16px;
  }
  .firm .dot {
    width: 40px; height: 40px;
    border: 2px solid var(--ink);
    border-radius: 50%;
    flex: none;
  }
  .firm-name {
    font-family: var(--serif);
    font-size: 19px;
    line-height: 1.15;
    text-transform: uppercase;
    letter-spacing: .03em;
  }
  .rule {
    height: 1px;
    background: var(--gold);
    margin: 22px 0 16px;
  }
  .person-name {
    color: var(--gold);
    font-size: 21px;
    letter-spacing: .06em;
    text-transform: uppercase;
  }
  .person-title { font-size: 15px; margin-bottom: 14px; }
  .contact { list-style: none; font-size: 14.5px; line-height: 1.55; }
  .contact li { display: flex; align-items: center; gap: 8px; }
  .contact .icon { width: 16px; height: 16px; flex: none; }
  .contact .plain { padding-left: 24px; }
  .contact .web { color: var(--gold); padding-left: 24px; }
</style>
</head>
<body>
  <section class="card card-back" aria-label="Business card back">
    <div class="back-mark"><span class="dot"></span>Willowcrest</div>
    <p class="back-message">If you have been arrested for any<br>criminal offense, do not hesitate<br>to contact our law offices.</p>
  </section>

  <section class="card card-front" aria-label="Business card front">
    <div class="firm">
      <span class="dot"></span>
      <h1 class="firm-name">Willowcrest Criminal<br>Law Offices</h1>
    </div>
    <div class="rule"></div>
    <h2 class="person-name">Dana Vorhees</h2>
    <p class="person-title">Attorney</p>
    <ul class="contact">
      <li>
        <svg class="icon" viewBox="0 0 16 16" aria-hidden="true"><circle cx="8" cy="8" r="8" fill="#1b9aaa"/><path d="M5.2 4.2l1.4-.3.8 2-1 .8a5 5 0 0 0 2.4 2.4l.8-1 2 .8-.3 1.4c-3.6.3-6.4-2.5-6.1-6.1z" fill="#fff"/></svg>
        505.555.0147
      </li>
      <li>
        <svg class="icon" viewBox="0 0 16 16" aria-hidden="true"><circle cx="8" cy="8" r="8" fill="#1b9aaa"/><rect x="4" y="5.2" width="8" height="5.6" fill="none" stroke="#fff" stroke-width="1.1"/><path d="M4 5.4l4 3 4-3" fill="none" stroke="#fff" stroke-width="1.1"/></svg>
        dvorhees@willowcresttrialdesk.com
      </li>
      <li class="plain">2140 Alder Row NW, Willowcrest, NM 87000</li>
      <li class="web">www.willowcresttrialdesk.com</li>
    </ul>
  </section>
</body>
</html>
```